website re-design

require to re design my existing website ( www.lunarfoxgrove.example ) to show a corporate image of the company . i also require an advise on the content editorial text . i am currently using pel wimbo for domain registration and website design and publishing .

Target Market(s)

focus on the meddle east market , but visible for worldwide business opportunity

Industry/Entity Type

It Company

Coding

Coded - Design and coding required

Number of Pages Required

5+ page

Requirements
Must have
• --show the brand color when possible ,
• --professional website reflecting the following main key areas :broadcast /media/consultancy services/technology
• --number of pages to be maintained or increased if necessary
• --adaptive design for all PC and mobiles
• --simple to navigate and get the idea quickly
• --landing page with full image and slight movement in the background
Nice to have
• any interactivity with visitors
• font style to be recommended by the designer ( professional test , easy to read )
• more descriptive image and less text
• visitor to know what we do more from graphics , image and video
• landing page to have some motions ( similar to www.harbortwillco.example/ )

```html
<!DOCTYPE html>
<html lang="en">
<head>
<meta charset="utf-8">
<title>Lunar Fox Grove</title>
<link href="https://fonts.googleapis.com/css2?family=Raleway:wght@300;400;600;700&family=Open+Sans:wght@400;600&display=swap" rel="stylesheet">
<style>
:root{
  --orange:#ef6c0b;
  --orange-dark:#d85f06;
  --ink:#222;
  --muted:#777;
  --grey-bg:#ececec;
  --light-bg:#f3f3f3;
  --footer:#333;
  --white:#fff;
}
*{box-sizing:border-box;margin:0;padding:0}
html,body{width:1200px;height:3226px;overflow:hidden}
body{position:relative;background:var(--white);font-family:"Open Sans",Arial,sans-serif;color:var(--ink)}
.abs{position:absolute}

/* header */
.site-header{left:0;top:0;width:1200px;height:133px;background:var(--white);border-bottom:3px solid var(--orange)}
.brand{left:90px;top:0;width:125px;height:125px;background:var(--orange);color:var(--white);font-family:"Raleway",sans-serif;font-weight:600;font-size:21px;line-height:22px;padding:34px 10px 0 10px}
.phone{left:823px;top:30px;font-size:17px;color:#333;display:flex;align-items:center;gap:10px}
.social{top:21px;display:flex;gap:8px;left:985px}
.social span{width:40px;height:40px;border-radius:50%;background:var(--orange);display:block}
.main-nav{left:290px;top:86px;display:flex;font-family:"Raleway",sans-serif;font-size:17px;color:#333}
.main-nav a{margin-right:38px;text-decoration:none;color:#333}
.main-nav a.active{color:var(--orange)}

/* hero */
.hero{left:0;top:136px;width:1200px;height:541px;background:linear-gradient(120deg,#1e3b63 0%,#6a7684 35%,#b7b9bd 60%,#6e6460 85%,#2c2a2c 100%)}
.hero-band{left:0;top:331px;width:1200px;height:100px;background:rgba(0,0,0,.35)}
.hero-title{left:0;top:338px;width:1200px;text-align:center;color:var(--white);font-family:"Raleway",sans-serif;font-weight:700;font-size:60px;letter-spacing:1px}
.btn{background:var(--orange);color:var(--white);font-family:"Raleway",sans-serif;text-align:center;font-size:21px}
.hero-btn{left:495px;top:440px;width:210px;height:55px;line-height:55px}

/* feature cards */
.card{top:590px;width:338px;background:var(--white);padding:8px}
.card .photo{height:212px}
.card p{font-family:"Raleway",sans-serif;font-size:18px;line-height:27px;color:#333;padding:18px 0 0 0;width:285px}

/* welcome */
.section-title{left:0;width:1200px;text-align:center;color:var(--orange);font-family:"Raleway",sans-serif;font-weight:400;font-size:42px}
.intro{left:140px;top:986px;width:920px;text-align:center;font-size:14px;line-height:26px;color:#666}
.know-btn{left:512px;top:1133px;width:176px;height:54px;line-height:54px}

/* services */
.services{left:0;top:1251px;width:1200px;height:624px;background:var(--grey-bg)}
.services-intro{left:190px;top:1368px;width:820px;text-align:center;font-size:14.5px;line-height:26px;color:#444}
.service{top:1436px;width:252px;text-align:center}
.service .photo{height:166px}
.service h3{font-family:"Raleway",sans-serif;font-weight:400;font-size:19px;line-height:26px;color:#222;margin-top:20px}
.service p{font-size:13.5px;line-height:23px;color:#777;margin-top:10px;padding:0 6px}
.view-btn{left:522px;top:1769px;width:157px;height:56px;line-height:56px}

/* solutions */
.solutions{left:0;top:1875px;width:1200px;height:417px;background:var(--orange)}
.sol-title{left:77px;top:1908px;color:var(--white);font-family:"Raleway",sans-serif;font-size:42px;font-weight:400}
.sol-text{left:77px;top:1985px;width:540px;color:var(--white);font-size:13.5px;line-height:23px}
.sol-list{left:77px;top:2042px;list-style:none;color:var(--white);font-size:13.5px}
.sol-list li{height:29px;display:flex;align-items:center;gap:12px}
.sol-list li::before{content:"";width:8px;height:8px;background:var(--white)}
.sol-visual{left:628px;top:1978px;width:494px;height:290px;background:linear-gradient(90deg,#3a3a3a,#8c8c8c 50%,#3a3a3a)}

/* news & contact */
.col-title{top:2335px;color:var(--orange);font-family:"Raleway",sans-serif;font-size:40px;font-weight:400}
.news{left:77px;width:500px;height:110px}
.date{left:0;top:0;width:95px;height:97px;background:var(--light-bg);border:1px solid #ddd}
.date b{display:block;text-align:center;font-weight:400;font-size:32px;color:#333;margin-top:10px}
.date span{position:absolute;left:10px;bottom:-6px;width:75px;height:28px;line-height:28px;background:var(--orange);color:var(--white);text-align:center;font-size:14px}
.news h4{position:absolute;left:109px;top:0;font-weight:400;font-size:14px;line-height:20px;color:#222;white-space:nowrap;letter-spacing:-0.1px}
.news p{position:absolute;left:109px;top:22px;width:390px;font-size:14px;line-height:22px;color:#666}
.news em{position:absolute;left:109px;top:81px;font-size:13px;font-weight:600;color:var(--orange)}
.field{left:623px;width:497px;height:41px;background:#eee;border:1px solid #d8d8d8;font-size:14px;color:#777;padding:10px 12px;display:flex;justify-content:space-between}
.field svg{fill:#999}
.submit-btn{left:623px;top:2672px;width:155px;height:54px;line-height:54px}

/* partners */
.partners{left:0;top:2801px;width:1200px;height:138px;background:var(--light-bg);display:flex;align-items:center;justify-content:space-around;padding:0 60px;font-family:"Raleway",sans-serif;font-weight:600;font-size:34px;color:#2b2b2b}

/* footer */
.footer{left:0;top:2939px;width:1200px;height:228px;background:var(--footer)}
.foot-nav{left:77px;top:2960px;display:flex;align-items:center;font-size:15px;color:#ddd}
.foot-nav a{color:#ddd;text-decoration:none;margin-right:26px}
.foot-nav a.active{background:var(--orange);color:var(--white);padding:13px 24px;margin-right:32px}
.foot-social{left:980px;top:2958px;display:flex;gap:10px}
.foot-social span{width:40px;height:40px;border-radius:50%;background:var(--orange);display:block}
.foot-label{left:77px;top:3038px;color:var(--orange);font-size:18px}
.contact-item{top:3076px;display:flex;gap:16px;color:#bbb;font-size:14.5px;line-height:22px}
.icon-circle{width:48px;height:48px;border-radius:50%;flex:none;display:flex;align-items:center;justify-content:center}
.icon-circle.solid{background:var(--orange)}
.icon-circle.ring{border:2px solid var(--orange)}
.contact-item .txt{padding-top:12px}
.copyright{left:0;top:3167px;width:1200px;height:59px;background:var(--orange);color:#2a2a2a;font-size:14px;text-align:center;line-height:59px}
.copyright b{font-weight:600}
</style>
</head>
<body>

<header class="abs site-header">
  <div class="abs brand">LUNAR<br>FOX<br>GROVE</div>
  <div class="abs phone">
    <svg width="22" height="22" viewBox="0 0 24 24"><path fill="#ef6c0b" d="M6.6 10.8c1.4 2.8 3.8 5.1 6.6 6.6l2.2-2.2c.3-.3.7-.4 1-.2 1.1.4 2.3.6 3.6.6.6 0 1 .4 1 1V20c0 .6-.4 1-1 1C10.6 21 3 13.4 3 4c0-.6.4-1 1-1h3.5c.6 0 1 .4 1 1 0 1.3.2 2.5.6 3.6.1.3 0 .7-.2 1z"/></svg>
    9714 5550172
  </div>
  <div class="abs social"><span></span><span></span><span></span></div>
  <nav class="abs main-nav">
    <a class="active" href="#">HOME</a><a href="#">ABOUT</a><a href="#">SERVICES</a><a href="#">SOLUTIONS</a><a href="#">CUSTOMERS</a><a href="#">EMPLOYMENTS</a><a href="#" style="margin-right:0">CONTACT</a>
  </nav>
</header>

<section class="abs hero" role="img" aria-label="Hand touching floating digital media screens and growth charts"></section>
<div class="abs hero-band"></div>
<h1 class="abs hero-title">LUNAR FOX GROVE</h1>
<div class="abs btn hero-btn">SEND YOUR CV</div>

<div class="abs card" style="left:72px">
  <div class="photo" role="img" aria-label="Business team meeting in a bright office" style="background:linear-gradient(135deg,#dfe6ee,#8fa3b8 60%,#3c4c60)"></div>
  <p>Consultancy and Project Management</p>
</div>
<div class="abs card" style="left:429px">
  <div class="photo" role="img" aria-label="Engineer with digital network interface overlay" style="background:linear-gradient(135deg,#1c2c44,#4f7aa3 55%,#a9c6de)"></div>
  <p>Engineering and Managed Services</p>
</div>
<div class="abs card" style="left:788px">
  <div class="photo" role="img" aria-label="Broadcast camera filming a live stage event" style="background:linear-gradient(135deg,#6d8ab0,#2a3243 55%,#0f1218)"></div>
  <p>Innovative Broadcast Technology Solutions</p>
</div>

<h2 class="abs section-title" style="top:915px">WELCOME TO LUNAR FOX GROVE</h2>
<p class="abs intro">Lunar Fox Grove Provides Broadcast System Solutions and Services to support broadcasters , production house, telecom and satellite operator to achieve their goals of media innovation and operation efficiency through strategic planning and smart investment relying on innovative technologies  solutions and professional Services .<br>Lunar Fox Grove is a Technology solution and service provider in the broadcast and telecom media industry . Our objective is to support broadcasters, production house and telecom operators in their migration plan and developing new concepts and</p>
<div class="abs btn know-btn">KNOW MORE</div>

<section class="abs services"></section>
<h2 class="abs section-title" style="top:1286px">OUR BEST SERVICES</h2>
<p class="abs services-intro">We understand the media and entertainment industry and can help guide you through the technology change.  We have extensive real-world experience and practice in the broadcast.</p>

<div class="abs service" style="left:77px">
  <div class="photo" role="img" aria-label="Broadcast control room with wall of monitors" style="background:linear-gradient(135deg,#5a6468,#20272b 60%,#0c0f12)"></div>
  <h3>Studio and Broadcast<br>Facility Design</h3>
  <p>We understand the media &amp; entertainment industry and can help guide you through the technology.</p>
</div>
<div class="abs service" style="left:342px">
  <div class="photo" role="img" aria-label="Hand selecting from a fan of media screens" style="background:linear-gradient(135deg,#eef1f4,#9aa6b2 55%,#2f3a45)"></div>
  <h3>Technology Budget<br>Development</h3>
  <p>We understand the media &amp; entertainment industry and can help guide you through the technology.</p>
</div>
<div class="abs service" style="left:607px">
  <div class="photo" role="img" aria-label="Hands using a tablet with floating app icons" style="background:linear-gradient(135deg,#cfe6f2,#6fb1d6 55%,#2d6d98)"></div>
  <h3>Develop &amp; Manage<br>RFP's</h3>
  <p>We understand the media &amp; entertainment industry and can help guide you through the technology.</p>
</div>
<div class="abs service" style="left:871px">
  <div class="photo" role="img" aria-label="Colleagues working together at office computers" style="background:linear-gradient(135deg,#e9e6e2,#b8aea4 55%,#6f6660)"></div>
  <h3>Program/Project<br>Management</h3>
  <p>We understand the media &amp; entertainment industry and can help guide you through the technology.</p>
</div>
<div class="abs btn view-btn">VIEW ALL</div>

<section class="abs solutions"></section>
<h2 class="abs sol-title">OUR SOLUTIONS</h2>
<p class="abs sol-text">Our goal is to provide creative and competitive technology solutions that enable to grow your business in a cost effective way and in line with business strategy.</p>
<ul class="abs sol-list">
  <li>HBBTV and interactive applications for TV and 2nd screen</li>
  <li>Digital and online media distribution and contribution</li>
  <li>Satellite distribution and contribution compression systems</li>
  <li>End to End OTT platforms</li>
  <li>End to end channel playout and distribution</li>
  <li>Disaster recovery in the cloud</li>
  <li>Augmented reality solutions</li>
</ul>
<div class="abs sol-visual" role="img" aria-label="Curved wall of video thumbnails with a hand touching a screen"></div>

<h2 class="abs col-title" style="left:77px">LATEST NEWS</h2>
<h2 class="abs col-title" style="left:621px">CONTACT US</h2>

<article class="abs news" style="top:2419px">
  <div class="abs date"><b>04</b><span>Nov</span></div>
  <h4>Storage Trends Exploring Objects and Scale-Out NAS</h4>
  <p>Network attached storage, or NAS, continues to expand in acceptance and in capabilities.</p>
  <em>READ MORE</em>
</article>
<article class="abs news" style="top:2533px">
  <div class="abs date"><b>03</b><span>Nov</span></div>
  <h4>Don't Forget: Deadline to File EAS Form Three Is Nov.14</h4>
  <p>While most of the U.S. population may experience election fatigue, broadcasters may be forgiven.</p>
  <em>READ MORE</em>
</article>
<article class="abs news" style="top:2649px">
  <div class="abs date"><b>03</b><span>Nov</span></div>
  <h4>Bird Conservancy Hails Tower Changes</h4>
  <p>A bird conservation group estimates that approx - imately 750 tall towers in the United States.</p>
  <em>READ MORE</em>
</article>

<div class="abs field" style="top:2419px">Name*<svg width="16" height="16" viewBox="0 0 16 16"><circle cx="8" cy="5" r="3.5"/><path d="M1 16c0-4 3-6 7-6s7 2 7 6z"/></svg></div>
<div class="abs field" style="top:2466px">Email*<svg width="17" height="14" viewBox="0 0 17 14"><rect x="0" y="1" width="17" height="12" rx="1"/><path d="M1 2l7.5 6L16 2" stroke="#eee" stroke-width="1.5" fill="none"/></svg></div>
<div class="abs field" style="top:2513px">Phone*<svg width="16" height="16" viewBox="0 0 24 24"><path d="M6.6 10.8c1.4 2.8 3.8 5.1 6.6 6.6l2.2-2.2c.3-.3.7-.4 1-.2 1.1.4 2.3.6 3.6.6.6 0 1 .4 1 1V20c0 .6-.4 1-1 1C10.6 21 3 13.4 3 4c0-.6.4-1 1-1h3.5c.6 0 1 .4 1 1 0 1.3.2 2.5.6 3.6.1.3 0 .7-.2 1z"/></svg></div>
<div class="abs field" style="top:2561px;height:101px;align-items:flex-start">Message*<svg width="18" height="15" viewBox="0 0 18 15"><ellipse cx="7" cy="6" rx="7" ry="5"/><ellipse cx="12" cy="9" rx="6" ry="4.5"/></svg></div>
<div class="abs btn submit-btn">SUBMIT</div>

<section class="abs partners">
  <span>Kestrel</span><span>Velora</span><span>Tarnwell</span><span>Quillon</span><span>Sarnet</span><span>ninefive31</span>
</section>

<footer class="abs footer"></footer>
<nav class="abs foot-nav">
  <a class="active" href="#">Home</a><a href="#">About</a><a href="#">Services</a><a href="#">Solutions</a><a href="#">Customer</a><a href="#">Employments</a><a href="#">Contact</a>
</nav>
<div class="abs foot-social"><span></span><span></span><span></span></div>
<div class="abs foot-label">CONTACT US</div>

<div class="abs contact-item" style="left:77px">
  <div class="icon-circle solid"><svg width="20" height="26" viewBox="0 0 20 26"><path fill="#fff" d="M10 0C4.5 0 0 4.3 0 9.6 0 16.8 10 26 10 26s10-9.2 10-16.4C20 4.3 15.5 0 10 0zm0 13a3.5 3.5 0 110-7 3.5 3.5 0 010 7z"/></svg></div>
  <div class="txt" style="width:190px;padding-top:4px">Harbor Media Park HMP 2, Quay Bld , 2nd floor, Box 100482</div>
</div>
<div class="abs contact-item" style="left:352px">
  <div class="icon-circle ring"><svg width="20" height="20" viewBox="0 0 24 24"><path fill="#ef6c0b" d="M6.6 10.8c1.4 2.8 3.8 5.1 6.6 6.6l2.2-2.2c.3-.3.7-.4 1-.2 1.1.4 2.3.6 3.6.6.6 0 1 .4 1 1V20c0 .6-.4 1-1 1C10.6 21 3 13.4 3 4c0-.6.4-1 1-1h3.5c.6 0 1 .4 1 1 0 1.3.2 2.5.6 3.6.1.3 0 .7-.2 1z"/></svg></div>
  <div class="txt">+971-555-01720</div>
</div>
<div class="abs contact-item" style="left:592px">
  <div class="icon-circle ring"><svg width="20" height="20" viewBox="0 0 20 20"><rect x="2" y="7" width="16" height="10" rx="1" fill="#ef6c0b"/><rect x="5" y="2" width="10" height="6" fill="none" stroke="#ef6c0b" stroke-width="2"/></svg></div>
  <div class="txt">+97-15550-18834</div>
</div>
<div class="abs contact-item" style="left:858px">
  <div class="icon-circle ring"><svg width="20" height="16" viewBox="0 0 20 16"><rect x="0" y="1" width="20" height="14" rx="1" fill="#ef6c0b"/><path d="M1 2l9 7 9-7" stroke="#333" stroke-width="1.6" fill="none"/></svg></div>
  <div class="txt">info@lunarfoxgrove.example</div>
</div>

<div class="abs copyright">© <b>LUNAR FOX GROVE</b> 2016. All Rights Reserved</div>

</body>
</html>
```